依頼詳細
本チラシの利用シーンは、各大学の就職課・キャリアセンターへ配布したり、掲示板等に掲載してもらう予定です。
先生方へお渡しして、ゼミや研究室の学生に配布してもらったり、企業説明会で学生に直接配布する事も想定されます。弊社のホームページにも掲載の予定です。
数あるインターンシップ講座の中から、下記イメージやキーワードを目にしたときに興味を引いてもらえるようなデザインを希望します。
チラシの構成(配置)イメージを添付いたしますので、参考にしてください。
また、デザインの際にはこちらで選びました2種類の写真(別途添付)を使用してください。大きさや配置などはお任せいたします。(写真はデザイン確定後購入予定の為、ダミーです。)

<希望イメージ、キーワード>
・ IT系の会社で、『システム開発のインターンシップ』という事がひと目でわかる。
・ すっきり見やすく(絵やデザインがごちゃごちゃしていない)、さわやかなデザイン。
・ 学生目線で、親近感がわくデザインを希望します。
記載項目
下記内容は必ず記載してください。
<インターンシップ概要>
○実施期間 7月 27日(金) 8月3日(金)・10日(金) 9月7日(金)・14日(金)
※上記日程の内、いづれか1日
○募集締切 実施日の1週間前までに書類必着
○実施内容 アプリ開発で使用される人気のプログラミング言語 ”JavaScript” を使用して、全国の多くの地方自治体で利用している「文書管理システム」の開発疑似体験をしていただきます。
IT業界を知ることから、オリジナルのプログラムを通じてSEに必要とされるスキル・考え方を体感いただける内容をご用意しています。
※JavaScript言語はさほど難しいものではありませんのでプログラム経験のない方でもご参加いただけます。
○応募対象 大学院、大学、専門学校、高専に在学中のソフトウェア開発に興味がある学生
(学部、学科問わず)
○応募方法 メールにて以下の内容を記載の上、総務部)インターンシップ担当 saiyo@ktv-ltd.example.jp
宛までお送り下さい。
・名前・住所・生年月日・連絡先(携帯番号・メールアドレス)・学校名(学部学科学年)・志望理由
サイズ
A4
ページ数
片面
希望イメージ
シンプル 複雑
単色 カラフル
暗い 明るい
日常 高級
遊び心 厳粛
未来的 伝統的
女性的 男性的
希望する色
青系、水色系
納品ファイル
• イラストレーター形式 (.ai)
補足説明
※記載項目の続き

○個人情報の取り扱い ご提出いただいた個人情報はインターンシップの選考および応募者へのご連絡以外
の目的では使用いたしません。全ての個人情報は一定の保存期間経過後、弊社が責任をもって廃棄いたします。
○ ロゴマーク
○ キャッチフレーズ  誰でも作れる!業務アプリケーション開発 インターンシップ生募集!

<会社情報>
株式会社ケイ・ティ・ブイ
〒190-0047 東京都立川市栄町4-2-9 桐原栄町ビル3階
問合せ先TEL. 042-561-7304

<QRコード> (会社HPトップ画面に誘導)

※期間、締切は大きく目立つように入れて下さい。
※実施期間は修正可能なようにしてください。

今回採用させていただいたご提案は、掲示された際に目を引くという事と、男女問わず親近感が沸くイラストデザインだった事がポイントです。

この度は、多数のご応募誠にありがとうございました。
どのご提案もこちらの要望や依頼事項を汲み取って頂き、洗練されたデザインばかりでした。
はじめてのコンペで不慣れな点もあったかと思いますが、たくさんのご提案を拝見する事ができて大変感激しています。

```html
<!DOCTYPE html>
<html lang="ja">
<head>
<meta charset="utf-8">
<title>業務アプリケーション開発インターンシップ生募集</title>
<link href="https://fonts.googleapis.com/css2?family=Noto+Sans+JP:wght@400;500;700;900&display=swap" rel="stylesheet">
<style>
:root{
  --blue:#1a8fd6;
  --sky:#43b3ea;
  --navy:#0f3f7a;
  --ink:#333;
  --line:#cfe3f1;
  --white:#fff;
}
*{margin:0;padding:0;box-sizing:border-box}
html,body{width:846px;height:1200px;overflow:hidden;background:var(--white)}
body{font-family:"Noto Sans JP",sans-serif;color:var(--ink);position:relative}
.brand-bar{position:absolute;top:0;left:0;width:846px;height:60px;background:var(--white);display:flex;align-items:center;padding-left:26px}
.brand-name{font-weight:900;font-size:34px;color:var(--blue);letter-spacing:2px}
.hero-photo{position:absolute;top:60px;left:0;width:846px;height:470px;background:linear-gradient(160deg,#dfe9f0 0%,#c5d6e3 45%,#e9eef2 100%)}
.hero-bubble{position:absolute;top:250px;left:560px;width:260px;height:112px;background:var(--blue);border-radius:14px;color:var(--white);font-weight:700;font-size:31px;line-height:1.35;text-align:center;padding-top:15px}
.hero-bubble svg{position:absolute;left:40px;bottom:-22px}
.headline{position:absolute;top:548px;left:0;width:846px;text-align:center;color:var(--navy);font-weight:900;line-height:1.35}
.headline .line1{font-size:34px;letter-spacing:1px}
.headline .accent{color:var(--blue)}
.headline .line2{font-size:32px}
.schedule{position:absolute;top:650px;left:30px;width:786px;display:flex;justify-content:space-between}
.slot{width:118px;text-align:center}
.slot-badge{width:100px;height:100px;margin:0 auto;border-radius:50%;background:var(--sky);color:var(--white);display:flex;flex-direction:column;align-items:center;justify-content:center;font-weight:700;line-height:1.15}
.slot-badge .month{font-size:18px}
.slot-badge .day{font-size:29px}
.slot-badge .day small{font-size:16px}
.slot-head .slot-badge{background:var(--navy);font-size:23px}
.deadline{margin-top:8px;font-size:18px;font-weight:700;color:var(--navy)}
.slot-head .deadline{background:var(--navy);color:var(--white);border-radius:4px;padding:1px 0;font-size:16px}
.details{position:absolute;top:800px;left:30px;width:786px;display:flex;gap:30px}
.col{flex:1}
.sec-title{display:flex;align-items:center;gap:8px;font-size:20px;font-weight:700;color:var(--blue);margin-bottom:4px}
.sec-title i{width:16px;height:16px;border-radius:50%;background:var(--blue);display:inline-block}
.sec-body{font-size:12.5px;line-height:1.6}
.sec-body + .sec-title{margin-top:10px}
.items{display:grid;grid-template-columns:92px 1fr;gap:5px 10px;margin-top:8px;font-size:12.5px}
.items li{list-style:none;display:flex;align-items:center;gap:6px}
.items li svg{flex:none}
.footer{position:absolute;left:0;bottom:0;width:846px;height:92px;border-top:2px solid var(--line);background:var(--white);display:flex;align-items:center;justify-content:space-between;padding:0 30px}
.company{font-size:12.5px;line-height:1.55}
.company .name{font-size:15px;font-weight:700;color:var(--navy)}
.contact-web{display:flex;align-items:center;gap:14px}
.url{font-size:15px;font-weight:700;color:var(--navy)}
.qr-area{width:64px;height:64px;border:2px solid var(--navy);background:#f2f6f9}
</style>
</head>
<body>
<header class="brand-bar"><span class="brand-name">KTV</span></header>
<div class="hero-photo" role="img" aria-label="オフィスで学生たちがノートパソコンを囲んで話し合う写真"></div>
<div class="hero-bubble">システム開発<br>の仕事って?
  <svg width="36" height="24" viewBox="0 0 36 24"><path d="M0 0H36L8 24Z" fill="#1a8fd6"/></svg>
</div>

<section class="headline">
  <p class="line1"><span class="accent">誰でも作れる!</span>業務アプリケーション</p>
  <p class="line2">開発インターンシップ生募集!</p>
</section>

<section class="schedule">
  <div class="slot slot-head"><div class="slot-badge">実施日</div><p class="deadline">募集締切</p></div>
  <div class="slot"><div class="slot-badge"><span class="month">7月</span><span class="day">27<small>(金)</small></span></div><p class="deadline">7/20(金)</p></div>
  <div class="slot"><div class="slot-badge"><span class="month">8月</span><span class="day">3<small>(金)</small></span></div><p class="deadline">7/27(金)</p></div>
  <div class="slot"><div class="slot-badge"><span class="month">8月</span><span class="day">10<small>(金)</small></span></div><p class="deadline">8/3(金)</p></div>
  <div class="slot"><div class="slot-badge"><span class="month">9月</span><span class="day">7<small>(金)</small></span></div><p class="deadline">8/31(金)</p></div>
  <div class="slot"><div class="slot-badge"><span class="month">9月</span><span class="day">14<small>(金)</small></span></div><p class="deadline">9/7(金)</p></div>
</section>

<section class="details">
  <div class="col">
    <h2 class="sec-title"><i></i>実施内容</h2>
    <p class="sec-body">アプリ開発で使用される人気のプログラミング言語”JavaScript”を使用して、全国の多くの地方自治体で利用している「文書管理システム」の開発疑似体験をしていただきます。<br>IT業界を知ることから、オリジナルのプログラムを通じてSEに必要とされるスキル・考え方を体感いただける内容をご用意しています。<br>※JavaScript言語はさほど難しいものではありませんのでプログラム経験のない方でもご参加いただけます。</p>
  </div>
  <div class="col">
    <h2 class="sec-title"><i></i>応募対象</h2>
    <p class="sec-body">大学院、大学、専門学校、高専に在学中のソフトウェア開発に興味がある学生(学部、学科問わず)</p>
    <h2 class="sec-title"><i></i>応募方法</h2>
    <p class="sec-body">メールにて以下の内容を記載の上、総務部)インターンシップ担当 saiyo@ktv-ltd.example.jp 宛までお送り下さい。</p>
    <ul class="items">
      <li><svg width="13" height="13" viewBox="0 0 14 14"><rect width="14" height="14" rx="3" fill="#1a8fd6"/><path d="M3 7l3 3 5-6" stroke="#fff" stroke-width="2" fill="none"/></svg>名前</li>
      <li><svg width="13" height="13" viewBox="0 0 14 14"><rect width="14" height="14" rx="3" fill="#1a8fd6"/><path d="M3 7l3 3 5-6" stroke="#fff" stroke-width="2" fill="none"/></svg>連絡先(携帯番号・メールアドレス)</li>
      <li><svg width="13" height="13" viewBox="0 0 14 14"><rect width="14" height="14" rx="3" fill="#1a8fd6"/><path d="M3 7l3 3 5-6" stroke="#fff" stroke-width="2" fill="none"/></svg>住所</li>
      <li><svg width="13" height="13" viewBox="0 0 14 14"><rect width="14" height="14" rx="3" fill="#1a8fd6"/><path d="M3 7l3 3 5-6" stroke="#fff" stroke-width="2" fill="none"/></svg>学校名(学部学科学年)</li>
      <li><svg width="13" height="13" viewBox="0 0 14 14"><rect width="14" height="14" rx="3" fill="#1a8fd6"/><path d="M3 7l3 3 5-6" stroke="#fff" stroke-width="2" fill="none"/></svg>生年月日</li>
      <li><svg width="13" height="13" viewBox="0 0 14 14"><rect width="14" height="14" rx="3" fill="#1a8fd6"/><path d="M3 7l3 3 5-6" stroke="#fff" stroke-width="2" fill="none"/></svg>志望理由</li>
    </ul>
  </div>
</section>

<footer class="footer">
  <div class="company">
    <p class="name">株式会社ケイ・ティ・ブイ</p>
    <p>〒190-0047 東京都立川市栄町4-2-9 桐原栄町ビル3階</p>
    <p>問合せ先TEL. 042-561-7304</p>
  </div>
  <div class="contact-web">
    <p class="url">http://www.ktv-ltd.example.jp</p>
    <div class="qr-area" role="img" aria-label="会社ホームページへのQRコード"></div>
  </div>
</footer>
</body>
</html>
```